Business card for STEADYWAVE

Please design professional business card for IT consulting firm STEADYWAVE INC.
Use logo attached.
Use information from sample qNode business card attached.
replace qnode inc with STEADYWAVE INC.
as well as qnodeinc.com with steadywave.example

```html
<!DOCTYPE html>
<html lang="en">
<head>
<meta charset="utf-8">
<title>STEADYWAVE INC. business card</title>
<link rel="stylesheet" href="https://fonts.googleapis.com/css2?family=Montserrat:wght@700&family=Lato:wght@400;900&display=swap">
<style>
  :root {
    --bg: #e9e7e4;
    --ink: #050505;
    --paper: #ffffff;
    --cyan: #4ab8e0;
    --teal: #5ecfc4;
    --orange: #f0922a;
    --purple: #9b4fb0;
    --text-light: #f2f2f2;
  }
  * { margin: 0; padding: 0; box-sizing: border-box; }
  html, body {
    width: 1200px; height: 900px; overflow: hidden;
    background: var(--bg);
  }
  .sheet {
    width: 1200px; height: 900px;
    display: flex; flex-direction: column; align-items: center; justify-content: center;
    gap: 54px;
  }
  .card {
    width: 600px; height: 343px; display: block;
    box-shadow: 0 6px 18px rgba(0,0,0,0.18);
  }
  .wordmark {
    font-family: "Montserrat", sans-serif; font-weight: 700;
    fill: var(--ink); letter-spacing: 3px;
  }
  .site-url {
    font-family: "Lato", sans-serif; font-weight: 400;
    fill: var(--cyan); letter-spacing: 8px;
  }
  .person-name {
    font-family: "Lato", sans-serif; font-weight: 900;
    fill: var(--cyan); letter-spacing: 0.5px;
  }
  .person-title, .contact-line, .address-line {
    font-family: "Lato", sans-serif; font-weight: 400;
    fill: var(--text-light);
  }
  .icon { fill: none; stroke: var(--orange); stroke-width: 1.6; }
  .icon-solid { fill: var(--orange); }
  .divider { stroke: var(--purple); stroke-width: 1.2; }
</style>
</head>
<body>
<main class="sheet">

  <!-- Front side -->
  <svg class="card card-front" viewBox="0 0 600 343" xmlns="http://www.w3.org/2000/svg">
    <defs>
      <linearGradient id="front-stripe" x1="0" y1="0" x2="0" y2="1">
        <stop offset="0" stop-color="#9b4fb0"/>
        <stop offset="0.25" stop-color="#6c7fd0"/>
        <stop offset="0.4" stop-color="#f0922a"/>
        <stop offset="0.6" stop-color="#4ab8e0"/>
        <stop offset="0.8" stop-color="#5ecfc4"/>
        <stop offset="0.92" stop-color="#b455b8"/>
        <stop offset="1" stop-color="#f0922a"/>
      </linearGradient>
    </defs>
    <rect class="card-paper" width="600" height="343" fill="var(--paper)"/>
    <polygon class="stripe" points="254,0 266,0 228,343 214,343" fill="url(#front-stripe)"/>
    <polygon class="ink-field" points="262,0 600,0 600,343 228,343" fill="var(--ink)"/>
    <polygon class="name-band" points="262,50 600,0 600,40 240,100 180,110 170,60" fill="var(--paper)"/>
    <text class="wordmark" x="168" y="110" font-size="33" transform="rotate(-8.4 168 110)">STEADYWAVE INC</text>
    <text class="site-url" x="575" y="305" font-size="19" text-anchor="end">www.steadywave.example</text>
  </svg>

  <!-- Back side -->
  <svg class="card card-back" viewBox="0 0 600 343" xmlns="http://www.w3.org/2000/svg">
    <defs>
      <linearGradient id="back-stripe" x1="0" y1="0" x2="1" y2="0">
        <stop offset="0" stop-color="#6c7fd0"/>
        <stop offset="0.2" stop-color="#f0922a"/>
        <stop offset="0.45" stop-color="#4ab8e0"/>
        <stop offset="0.7" stop-color="#5ecfc4"/>
        <stop offset="0.88" stop-color="#b455b8"/>
        <stop offset="1" stop-color="#f0922a"/>
      </linearGradient>
    </defs>
    <rect class="card-paper" width="600" height="343" fill="var(--paper)"/>
    <polygon class="top-wedge" points="0,0 260,0 0,35" fill="var(--ink)"/>
    <polygon class="stripe" points="300,40 600,228 600,244 296,47" fill="url(#back-stripe)"/>
    <polygon class="ink-field" points="0,80 300,46 600,244 600,343 0,343" fill="var(--ink)"/>
    <text class="wordmark" x="120" y="66" font-size="31" transform="rotate(-7.6 120 66)">STEADYWAVE INC</text>

    <g class="contact-block" transform="rotate(-4 40 160)">
      <text class="person-name" x="40" y="125" font-size="21">DORIAN VELASKO</text>
      <text class="person-title" x="42" y="145" font-size="13">P.ENG.</text>

      <rect class="icon" x="48" y="164" width="8" height="13" rx="1.5"/>
      <text class="contact-line" x="66" y="176" font-size="14">(416) 555-0148</text>
      <path class="icon-solid" d="M45 196 q7 -7 14 0 l-2 3 h-10 z M47 199 h10 v4 h-10 z"/>
      <text class="contact-line" x="66" y="202" font-size="14">(905) 555-0172 ext.201</text>

      <circle class="icon" cx="54" cy="230" r="5.5"/>
      <text class="contact-line" x="66" y="235" font-size="13.5">www.steadywave.example</text>
      <rect class="icon" x="48" y="249" width="12" height="8"/>
      <path class="icon" d="M48 249 l6 5 l6 -5"/>
      <text class="contact-line" x="66" y="258" font-size="13.5">dvelasko@steadywave.example</text>
    </g>

    <line class="divider" x1="40" y1="306" x2="560" y2="240"/>
    <g class="address" transform="rotate(-7.2 60 326)">
      <path class="icon-solid" d="M60 332 l-5 -8 a5.5 5.5 0 1 1 10 0 z"/>
      <circle cx="60" cy="321" r="1.8" fill="var(--ink)"/>
      <text class="address-line" x="72" y="330" font-size="13">2150 Harbourline Rd, Suite 101, Lakeview, Ontario, L0X 1A1, Canada</text>
    </g>
  </svg>

</main>
</body>
</html>
```